Corporate Design für ein Installationsunternehmen
Wir sind mit dem Endergebnis sehr glücklich und zufrieden! Ruvo ist auf alle unsere Wünsche und Vorschläge ohne zu zögern und mit viel Geduld eingegangen und wir können seine Arbeit wärmstens empfehlen. Vielen Dank nochmal Ruvo für das tolle Design.
Zielgruppe
Wir sind ein Installationsunternehmen im Bereich Gas-, Wasser- und Heizung.
Aufgabenstellung
Das Symbol des Triskele sollte im Logo kreativ integriert werden ( wir sind jedoch offen auch für andere kreative Vorschläge die uns inspirieren).
Sauber, akkurat, symmetrisch und professionell soll es rüber kommen.
Das Symbol soll Vertrauen im Kunden wecken.

```html
<!DOCTYPE html>
<html lang="de">
<head>
<meta charset="utf-8">
<title>Korventa – Geschäftsausstattung</title>
<link href="https://fonts.googleapis.com/css2?family=Raleway:wght@400;500;700&display=swap" rel="stylesheet">
<style>
  :root{
    --bg:#dcdcdc;
    --paper:#ececec;
    --paper-fold:#f2f2f2;
    --navy:#2f3a4b;
    --ink:#2a2f38;
    --muted:#555c66;
    --accent:#3584d4;
    --window:#d6d9dd;
  }
  *{box-sizing:border-box;margin:0;padding:0}
  html,body{width:1200px;height:858px;overflow:hidden;background:var(--bg)}
  body{position:relative;font-family:"Raleway",sans-serif;color:var(--ink)}

  .brand{display:flex;align-items:center;gap:6px;font-weight:700;letter-spacing:.02em;color:var(--ink)}
  .brand-dot{border-radius:50%;background:var(--accent);flex:none}

  .base-rule{position:absolute;left:0;bottom:0;width:100%;height:3px;background:var(--navy)}

  /* envelopes */
  .envelope{position:absolute;overflow:hidden}
  .envelope-dark{left:152px;top:429px;width:445px;height:210px;background:var(--navy)}
  .envelope-dark .brand{position:absolute;left:28px;top:42px;font-size:22px;color:#fff}
  .envelope-dark .brand-dot{width:18px;height:18px}
  .envelope-dark .window{position:absolute;right:36px;top:120px;width:120px;height:44px;background:var(--window);border-radius:3px}
  .envelope-dark .base-rule{background:#8a94a3}

  .envelope-light{left:62px;top:503px;width:448px;height:211px;background:var(--paper)}
  .envelope-light .brand{position:absolute;left:28px;top:55px;font-size:16px}
  .envelope-light .brand-dot{width:14px;height:14px}
  .envelope-light .window{position:absolute;right:32px;top:116px;width:130px;height:42px;background:var(--window);border:1px solid #c4c8cd;border-radius:3px}

  /* letterhead */
  .letter{position:absolute;left:638px;top:173px;width:462px;height:548px;background:var(--paper);overflow:hidden}
  .letter .fold{position:absolute;left:0;top:187px;width:100%;height:183px;background:var(--paper-fold)}
  .letter .brand{position:absolute;left:40px;top:44px;font-size:16px}
  .letter .brand-dot{width:14px;height:14px}
  .salutation{position:absolute;left:68px;top:143px;font-size:6.5px}
  .intro{position:absolute;left:96px;top:163px;width:270px;font-size:6.3px;line-height:1.35}
  .body-copy{position:absolute;left:55px;width:330px;font-size:6.3px;line-height:1.35}
  .body-copy.one{top:210px}
  .body-copy.two{top:288px}
  .closing{position:absolute;left:282px;top:392px;font-size:4.5px}
  .signature{position:absolute;left:283px;top:400px;width:80px;height:22px;background:linear-gradient(90deg,rgba(42,47,56,.18),rgba(42,47,56,.05));border-radius:3px}

  .footer{position:absolute;top:468px;left:34px;right:20px;display:flex;gap:18px;font-size:4.3px;line-height:1.3;letter-spacing:.03em;color:var(--muted);text-transform:uppercase}
  .footer p+p{margin-top:5px}
  .footer .col-a{width:158px}
  .footer .col-b{width:100px}
  .footer .col-c{width:120px;padding-top:9px}
  .footer dl{display:grid;grid-template-columns:30px auto;margin-top:8px}
</style>
</head>
<body>

<section class="envelope envelope-dark">
  <div class="brand"><span class="brand-dot"></span>KORVENTA</div>
  <div class="window"></div>
  <div class="base-rule"></div>
</section>

<section class="envelope envelope-light">
  <div class="brand"><span class="brand-dot"></span>KORVENTA</div>
  <div class="window"></div>
  <div class="base-rule"></div>
</section>

<article class="letter">
  <div class="fold"></div>
  <div class="brand"><span class="brand-dot"></span>KORVENTA</div>

  <p class="salutation">Dear Sir/ Madam,</p>
  <p class="intro">Korventa Gas Wasser Heizung Korventa Gas Wasser Heizung Korventa Gas Wasser Heizung. Describe what your company or organization does. Who is your target-audience?</p>

  <p class="body-copy one">Korventa Gas Wasser Heizung Korventa Gas Wasser Heizung Korventa Gas Wasser Heizung. Describe what your company or organization does. Who is your target-audience? Wir sind ein Installationsunternehmen im Bereich Gas-, Wasser- und Heizung. Das Symbol des Triskele sollte im Logo kreativ integriert werden (wir sind jedoch offen auch für andere kreative Vorschläge die uns inspirieren). Sauber, akkurat, symmetrisch und professionell soll es rüber kommen. Das Symbol soll Vertrauen im Kunden wecken.</p>

  <p class="body-copy two">Korventa Gas Wasser Heizung Korventa Gas Wasser Heizung Korventa Gas Wasser Heizung. Describe what your company or organization does. Who is your target-audience? Wir sind ein Installationsunternehmen im Bereich Gas-, Wasser- und Heizung. Das Symbol des Triskele sollte im Logo kreativ integriert werden (wir sind jedoch offen auch für andere kreative Vorschläge die uns inspirieren). Sauber, akkurat, symmetrisch und professionell soll es rüber kommen. Das Symbol soll Vertrauen im Kunden wecken.</p>

  <p class="closing">Your Sincerly</p>
  <div class="signature" role="img" aria-label="Handschriftliche Unterschrift von L. Vorbach"></div>

  <footer class="footer">
    <div class="col-a">
      <p>Korventa Haustechnik GmbH<br>– Meisterbetrieb Installation –</p>
      <p>Geschäftsführende Gesellschafter:<br>Lena Vorbach / Dr. Tim Alsen</p>
      <p>Technische Leitung: Lena Vorbach</p>
    </div>
    <div class="col-b">
      <p>Lindenweg 14<br>01234 Musterstadt</p>
      <dl>
        <dt>Telefon:</dt><dd>0123-456780</dd>
        <dt>Fax:</dt><dd>0123-456781</dd>
        <dt>Email:</dt><dd>info@korventa.de</dd>
        <dt>Web:</dt><dd>www.korventa.de</dd>
      </dl>
    </div>
    <div class="col-c">
      <p>Kontoverbindung:</p>
      <p>Steuernummer:<br>Musterbank eG<br>IBAN: DE00 1234 5678 9000 1122 33<br>BIC: MUSTDEXX</p>
    </div>
  </footer>

  <div class="base-rule"></div>
</article>

</body>
</html>
```